Modern and sophisticated web design for architect/designer

Lumo Vant is a Building Design & Drafting studio based in Carrow Heights Eastvale, providing a high quality and complete client service from concept design through Council planning approvals and building licenses to construction drawings for kitchens and bathrooms, extensions, additions, renovations and new homes.

Lumo Vant is looking for a new qwerty design that *is different from a normal* 2/3 column website. The website design must be very arty, clean and catchy. This design needs to be very different and must not look like a downloadable template.

The design must be able to display a lot of photos for the different projects.

The design must comply with W3C standards (i.e. use of fonts) and must be delivered to us in A PSD layered format.

Here are a couple of example website designs that exemplify what I am after:
1) http://www.prtd.com.au/
2) http://www.martinholsbyarchitect.com/en/
3) http://veromiks.com/

I particularly like numbers 1 and 2. The third, Veromiks, jumps around a little between pages as it is actually several companies. I prefer the page design to remain steady if possible.

I like the very clever nature of number 1 (PRTD). It captures the interest, although slightly gimmicky, however I think it doesn't overpower. Its modern, and visual.

I like the clean elegant design of number 2 (Holsby), it simply delivers everything necessary in a clear intelligent manner, its attractive, menu is clever simple to use and attractive.

I would be very happy to have either of these websites.

here is another one:
4) http://www.tqarchitect.com.au/

Although this is similarly elegant, it appears quite dated. I don't like the thumbnails that you click on in the gallery, its quite clumsy. It looks minimalist, and IS minimalist, doesn't look like there is much option to expand other than changing the pictures.

If you look at my own website:
http://www.lumovant.com.au

I designed and built it myself without any skills or experience. I had to use a generic photo album generator which was worse than useless, the point I am trying to make is I tried to make the menu system a little unusual, I tried to keep the pages neat and tidy, and totally used the "black website" method. However I am more inclined to go with the lighter/white pages of (1) and (2) above because they tend to show photos better.

Dear Designers. 

ArtHive Administration has worked to provide a more comprehensive brief. Please review the amended description. 

Kind Regards, Wesley. 

Target Market(s)

Target market is people who are looking to renovate their home

Industry/Entity Type

Construction

Requirements
Must have
• The brief is to design a visual modern, elegant, sophisticated website for a small scale designer/photographer/architect that looks itself like it is designed. Not off the shelf, simple and dated. Basically the design itself has to exemplify me, it has to say "this guy is a designer, and he is good at it".

```html
<!DOCTYPE html>
<html lang="en">
<head>
<meta charset="utf-8">
<title>Lumo Vant Design</title>
<link rel="stylesheet" href="https://fonts.googleapis.com/css2?family=PT+Sans+Narrow:wght@400;700&family=PT+Sans:ital,wght@0,400;0,700;1,400&display=swap">
<style>
  :root {
    --sky-top: #9fd0ee;
    --sky-mid: #d9eef9;
    --page: #ffffff;
    --ink: #2b2b2b;
    --ink-soft: #555555;
    --muted: #8a8a8a;
    --taupe: #ab9f9a;
    --taupe-dark: #4f4448;
    --green: #3c8a2e;
    --green-btn: #4a9a32;
    --field-border: #c9c9c9;
    --social: #8c9aa6;
  }
  * { box-sizing: border-box; margin: 0; padding: 0; }
  html, body { width: 989px; height: 1200px; overflow: hidden; }
  body {
    position: relative;
    font-family: "PT Sans", sans-serif;
    color: var(--ink);
    background:
      radial-gradient(ellipse 260px 60px at 120px 70px, rgba(255,255,255,.85), transparent 70%),
      radial-gradient(ellipse 300px 70px at 560px 80px, rgba(255,255,255,.8), transparent 70%),
      radial-gradient(ellipse 220px 60px at 900px 60px, rgba(255,255,255,.7), transparent 70%),
      linear-gradient(180deg, var(--sky-top) 0px, var(--sky-mid) 160px, #f4f9fc 420px, #ffffff 560px);
  }
  .abs { position: absolute; }

  /* Header */
  .brand { left: 86px; top: 30px; width: 260px; height: 70px; }
  .brand-name, .brand-sub { font-family: "PT Sans Narrow", sans-serif; font-weight: 700; font-size: 26px; letter-spacing: 6px; color: #3a3a3a; text-transform: uppercase; line-height: 1; }
  .brand-sub { margin: 10px 0 0 48px; }

  .search { left: 658px; top: 23px; width: 209px; height: 24px; display: flex; border: 1px solid #8e8e8e; border-radius: 3px; background: #fff; overflow: hidden; }
  .search-field { flex: 1; display: flex; align-items: center; gap: 8px; padding-left: 10px; font-size: 10px; color: var(--muted); }
  .search-go { width: 34px; background: linear-gradient(#6b6b6b, #444); color: #fff; font-size: 10px; display: flex; align-items: center; justify-content: center; }

  .nav { left: 554px; top: 71px; display: flex; align-items: center; height: 27px; font-size: 11px; color: #333; }
  .nav a { color: inherit; text-decoration: none; padding: 0 16px; height: 27px; display: flex; align-items: center; border-right: 1px solid rgba(0,0,0,.08); }
  .nav a:last-child { border-right: none; }
  .nav a.is-current { background: var(--taupe-dark); color: #fff; border-radius: 3px; padding: 0 13px; margin-right: 8px; border: none; }

  /* Main panel */
  .panel { left: 82px; top: 117px; width: 824px; height: 868px; background: var(--page); box-shadow: 0 2px 8px rgba(0,0,0,.12); }
  .slider { left: 91px; top: 125px; width: 809px; height: 301px; background: var(--taupe); box-shadow: 0 18px 30px -14px rgba(0,0,0,.35); }
  .slider-photo { left: 100px; top: 135px; width: 791px; height: 283px; background: linear-gradient(100deg, #6e3527 0%, #8a4a38 25%, #4a3a36 50%, #6a5650 70%, #cbb8a6 85%, #7d4a36 100%); }
  .slider-arrow { top: 249px; width: 51px; height: 51px; background: rgba(200,200,200,.55); display: flex; align-items: center; justify-content: center; }
  .slider-arrow.prev { left: 100px; }
  .slider-arrow.next { left: 839px; }
  .slider-caption { left: 107px; top: 309px; font-family: "PT Sans Narrow", sans-serif; font-weight: 700; font-size: 17px; line-height: 20px; color: #fff; text-shadow: 0 1px 2px rgba(0,0,0,.6); }

  .section-title { font-family: "PT Sans Narrow", sans-serif; font-size: 18px; text-transform: uppercase; line-height: 1; }
  .section-title span { font-weight: 400; color: #555; margin-right: 6px; }
  .section-title strong { font-weight: 700; color: #222; }

  .welcome-title { left: 99px; top: 470px; }
  .welcome-photo { left: 100px; top: 499px; width: 192px; height: 91px; border-radius: 3px; background: linear-gradient(135deg, #2e3a4a 0%, #8a5a2c 45%, #5a4030 70%, #3e5a2e 100%); }
  .welcome-text { left: 304px; top: 499px; width: 590px; }
  .lead { font-size: 10.5px; font-weight: 700; color: #222; margin-bottom: 5px; }
  .copy { font-size: 8.6px; line-height: 15px; color: var(--ink-soft); text-align: justify; }
  .welcome-text .copy { font-size: 8.3px; letter-spacing: -0.1px; }

  .btn { display: flex; align-items: center; justify-content: center; font-family: "PT Sans Narrow", sans-serif; font-size: 13px; color: #fff; text-decoration: none; }
  .btn-taupe { left: 822px; top: 587px; width: 66px; height: 26px; background: var(--taupe); }

  .services-title { left: 91px; top: 652px; }
  .services-arrows { left: 855px; top: 657px; display: flex; gap: 16px; }

  .service { top: 688px; width: 191px; }
  .service h3 { font-family: "PT Sans Narrow", sans-serif; font-weight: 700; font-size: 17px; color: var(--green); text-transform: uppercase; height: 30px; line-height: 20px; }
  .service-photo { width: 191px; height: 90px; border-radius: 2px; }
  .service h4 { font-size: 10px; font-weight: 700; color: #222; margin: 12px 0 6px 1px; }
  .service .copy { margin-left: 1px; }
  .btn-green { position: absolute; left: 122px; top: 237px; width: 66px; height: 26px; background: var(--green-btn); }

  /* Footer */
  .divider { left: 0; top: 1013px; width: 989px; border-top: 1px dotted #9a9a9a; }
  .contact-icon { left: 85px; top: 1026px; }
  .contact-title { left: 129px; top: 1033px; font-family: "PT Sans Narrow", sans-serif; font-weight: 700; font-size: 18px; color: #333; text-transform: uppercase; line-height: 1; }
  .field { border: 1px solid var(--field-border); border-radius: 2px; background: #fff; box-shadow: inset 0 1px 2px rgba(0,0,0,.08); font-size: 9px; font-style: italic; color: var(--muted); padding: 7px 12px; }
  .submit { left: 477px; top: 1131px; width: 80px; height: 32px; border-radius: 3px; background: linear-gradient(#5a5a5a, #111); font-family: "PT Sans Narrow", sans-serif; font-weight: 700; font-size: 14px; color: #fff; display: flex; align-items: center; justify-content: center; }

  .social { left: 721px; top: 1030px; display: flex; gap: 9px; }
  .social span { width: 22px; height: 22px; border-radius: 2px; background: var(--social); }
  .legal { right: 87px; top: 1068px; font-size: 9px; color: #444; }
  .legal a { color: inherit; text-decoration: none; }
  .legal i { font-style: normal; margin: 0 5px; color: #777; }
  .copyright { right: 87px; top: 1096px; font-size: 9px; color: #555; }
</style>
</head>
<body>

<header>
  <div class="abs brand">
    <div class="brand-name">Lumo Vant</div>
    <div class="brand-sub">Design</div>
  </div>

  <div class="abs search">
    <div class="search-field">
      <svg width="12" height="12" viewBox="0 0 12 12" aria-hidden="true"><circle cx="5" cy="5" r="3.6" fill="none" stroke="#888" stroke-width="1.3"/><line x1="7.6" y1="7.6" x2="11" y2="11" stroke="#888" stroke-width="1.6"/></svg>
      Search
    </div>
    <div class="search-go">GO</div>
  </div>

  <nav class="abs nav">
    <a href="#" class="is-current">Home</a>
    <a href="#">About Us</a>
    <a href="#">Services</a>
    <a href="#">Gallery</a>
    <a href="#">Contact Us</a>
  </nav>
</header>

<main>
  <div class="abs panel"></div>

  <div class="abs slider"></div>
  <div class="abs slider-photo" role="img" aria-label="Modern kitchen with timber floor, stone benchtops and red tiled splashback"></div>
  <div class="abs slider-arrow prev"><svg width="14" height="20" viewBox="0 0 14 20" aria-hidden="true"><polyline points="11,2 3,10 11,18" fill="none" stroke="#555" stroke-width="2.5"/></svg></div>
  <div class="abs slider-arrow next"><svg width="14" height="20" viewBox="0 0 14 20" aria-hidden="true"><polyline points="3,2 11,10 3,18" fill="none" stroke="#555" stroke-width="2.5"/></svg></div>
  <p class="abs slider-caption">Lumo Vant is a Building Design &amp; Drafting<br>studio based in Carrow Heights Eastvale,</p>

  <h2 class="abs section-title welcome-title"><span>Welcome to</span><strong>Lumo Vant Design</strong></h2>
  <div class="abs welcome-photo" role="img" aria-label="Timber deck and lit outdoor room at dusk"></div>
  <div class="abs welcome-text">
    <p class="lead">Mauris vel lacus vitae felis vestibulum volutpat. Etiam est nunc, venisl.</p>
    <p class="copy">Sed ut perspiciatis unde omnis iste natus error sit voluptatem accusantium doloremque laudantium, totam rem aperiam, eaque ipsa quae ab illo inventore veritatis et quasi architecto beatae vitae dicta sunt explicabo. Nemo enim ipsam voluptatem quia voluptas sit aspernatur aut odit aut fugit, sed quia consequuntur magni dolores eos qui ratione voluptatem sequi nesciunt. Neque porro quisquam est, qui dolorem ipsum quia dolor sit amet.Sed ut perspiciatis unde omnis iste natus error sit voluptatem accusantium doloremque laudantium, totam rem aperiam.</p>
  </div>
  <a href="#" class="abs btn btn-taupe">learn more</a>

  <h2 class="abs section-title services-title"><span>Our</span><strong>Services</strong></h2>
  <div class="abs services-arrows">
    <svg width="8" height="14" viewBox="0 0 8 14" aria-hidden="true"><polyline points="6,1 2,7 6,13" fill="none" stroke="#666" stroke-width="2"/></svg>
    <svg width="8" height="14" viewBox="0 0 8 14" aria-hidden="true"><polyline points="2,1 6,7 2,13" fill="none" stroke="#666" stroke-width="2"/></svg>
  </div>

  <article class="abs service" style="left:88px">
    <h3>Kitchens and Bathrooms</h3>
    <div class="service-photo" role="img" aria-label="Kitchen with stone benchtops and red splashback" style="background:linear-gradient(120deg,#5a3228,#8a5a46 45%,#b9a898 80%,#6a3a2a)"></div>
    <h4>Mauris vel lacus vestibulum volutpat.</h4>
    <p class="copy">Sed ut perspiciatis unde omnis iste natus error sit voluptatem accusantium doloremque laudantium, totam rem aperiam, eaque ipsa quae ab illo inventore veritatis et quasi architecto beatae vitae dicta sunt explicabo.</p>
    <a href="#" class="btn btn-green">learn more</a>
  </article>

  <article class="abs service" style="left:295px">
    <h3>Extensions</h3>
    <div class="service-photo" role="img" aria-label="Modern rendered extension with balcony" style="background:linear-gradient(120deg,#c7b8a4,#8a7a66 40%,#4a6fa8 75%,#8db2dd)"></div>
    <h4>Mauris vel lacus vestibulum volutpat.</h4>
    <p class="copy">Sed ut perspiciatis unde omnis iste natus error sit voluptatem accusantium doloremque laudantium, totam rem aperiam, eaque ipsa quae ab illo inventore veritatis et quasi architecto beatae vitae dicta sunt explicabo.</p>
    <a href="#" class="btn btn-green">learn more</a>
  </article>

  <article class="abs service" style="left:502px">
    <h3>Additions</h3>
    <div class="service-photo" role="img" aria-label="Sculptural curved glass addition" style="background:linear-gradient(120deg,#1c2030,#5a6a90 45%,#c8cde0 70%,#2a2f44)"></div>
    <h4>Mauris vel lacus vestibulum volutpat.</h4>
    <p class="copy">Sed ut perspiciatis unde omnis iste natus error sit voluptatem accusantium doloremque laudantium, totam rem aperiam, eaque ipsa quae ab illo inventore veritatis et quasi architecto beatae vitae dicta sunt explicabo.</p>
    <a href="#" class="btn btn-green">learn more</a>
  </article>

  <article class="abs service" style="left:709px">
    <h3>New Homes</h3>
    <div class="service-photo" role="img" aria-label="Two storey contemporary new home" style="background:linear-gradient(180deg,#5d8ed0,#a9c4e4 40%,#8a7a6a 70%,#4f6a3a)"></div>
    <h4>Mauris vel lacus vestibulum volutpat.</h4>
    <p class="copy">Sed ut perspiciatis unde omnis iste natus error sit voluptatem accusantium doloremque laudantium, totam rem aperiam, eaque ipsa quae ab illo inventore veritatis et quasi architecto beatae vitae dicta sunt explicabo.</p>
    <a href="#" class="btn btn-green">learn more</a>
  </article>
</main>

<footer>
  <div class="abs divider"></div>

  <svg class="abs contact-icon" width="36" height="34" viewBox="0 0 36 34" aria-hidden="true">
    <g transform="rotate(-14 18 17)">
      <rect x="4" y="7" width="28" height="20" fill="#fafafa" stroke="#bbb"/>
      <polyline points="4,7 18,19 32,7" fill="none" stroke="#bbb"/>
    </g>
  </svg>
  <h2 class="abs contact-title">Quick Contact</h2>

  <div class="abs field" style="left:92px;top:1072px;width:182px;height:26px">First Name</div>
  <div class="abs field" style="left:92px;top:1106px;width:182px;height:26px">Last Name</div>
  <div class="abs field" style="left:92px;top:1140px;width:182px;height:26px">Email</div>
  <div class="abs field" style="left:283px;top:1073px;width:183px;height:26px">Phone</div>
  <div class="abs field" style="left:283px;top:1107px;width:183px;height:59px;padding-top:12px">Comments</div>
  <div class="abs submit">SUBMIT</div>

  <div class="abs social" aria-label="Social links">
    <span></span><span></span><span></span><span></span><span></span><span></span>
  </div>
  <p class="abs legal"><a href="#">Privacy</a><i>|</i><a href="#">Terms of Use</a><i>|</i><a href="#">FAQ</a><i>|</i><a href="#">Contact Us</a></p>
  <p class="abs copyright">© 2013 lumovant.com.au, All rights reserved</p>
</footer>

</body>
</html>
```